Non-profit organisation for street children in Indonesia

Lentera Bocah provides home, education, family and health care for street children and other underprivileged children in Indonesia.

We need an emotional catchy advertisement that will make people aware of the terrible living conditions of street children in Indonesia and the great work the Lentera Bocah Foundation is doing to help these children.

We have 1 photo available for this advertisement. A little girl laying in the streets. This photo can be used with a strong quote such as "Street children whose responsibility?" or "Safer out on streets than at home" or "This child doesn't have the right to have a childhood worth remembering?" or another strong quote. Be creative! It need to touch people!

See some similar advertisements of other non-profit organizations what we very much like:

http://7brightpix.example/wp-content/uploads/2011/07/boldposters41.jpg
http://7brightpix.example/wp-content/uploads/2011/07/affiches-nobles-motifs-058.jpg

Mission
To give every child in the world the opportunity to live a happy and healthy life free of poverty, exploitation, and violence.

Overview
Lentera Bocah Foundation is an independent non-governmental organisation founded in 2005 in the Netherlands and expanded to Indonesia in 2006. Our aim is to improve the lives of children and to protect their rights by providing education, accommodation, family care and medical and legal aid.

Description
Lentera Bocah (Light for Youngsters) Foundation serves homeless and impoverished children by offering them a new path in life. By providing them with the necessary shelter, education, and psychological support directed towards vocational training, mentorship, and micro-credit opportunities, it strives to enable their re-entery into the community as happy and self-sufficient adults.

Facts:
There are 70 million children in Indonesia, nearly 18 million are very poor and estimated 170,000 children live on the streets.

Pitch submissions need to be 960x696 pixels.

Files available 1 photo and logo
Updates

Reason: Dear Designers, We have decided to extend the deadline because we haven't received what we are after. Please make a design in the trend as the following two examples: http://7brightpix.example/wp-content/uploads/2011/07/boldposters41.jpg http://7brightpix.example/wp-content/uploads/2011/07/affiches-nobles-motifs-058.jpg We hope to receive a good design shortly! Thank you Kind regards Lentera Bocah

Target Market(s)

Everybody

Industry/Entity Type

Non-Profit

Requirements
Must have
• 1. A strong quote.
2. Website url: www.lenterabocah.org
3. Mission quote from Lentera Bocah:
Should not have
• To much text.

```html
<!DOCTYPE html>
<html lang="en">
<head>
<meta charset="utf-8">
<title>Street Children – Lentera Bocah Foundation</title>
<link href="https://fonts.googleapis.com/css2?family=Rubik+Dirt&family=Arimo:wght@700&family=Open+Sans:wght@400;600&display=swap" rel="stylesheet">
<style>
  :root {
    --bg-green: #1a5e33;
    --bg-green-deep: #0f4526;
    --band-green: #138a47;
    --band-shadow: #0c6a35;
    --ad-yellow: #f0c419;
    --ink: #231f20;
    --cream: #f4efd2;
    --logo-yellow: #f6d41a;
    --white: #ffffff;
    --road-dark: #2b2b2d;
    --road-mid: #4a4a4c;
  }
  * { box-sizing: border-box; margin: 0; padding: 0; }
  html, body { width: 1114px; height: 1200px; overflow: hidden; }
  body {
    background: radial-gradient(ellipse at 50% 45%, var(--bg-green) 0%, var(--bg-green-deep) 100%);
    position: relative;
    font-family: "Arimo", Arial, sans-serif;
  }
  .ad {
    position: absolute; left: 59px; top: 222px; width: 1006px; height: 731px;
    background: var(--band-green);
    box-shadow: 0 6px 18px rgba(0,0,0,0.45);
    overflow: hidden;
  }
  .ad__photo {
    position: absolute; left: 0; top: 0; width: 1006px; height: 505px;
    background:
      radial-gradient(ellipse at 62% 68%, rgba(190,70,50,0.35) 0 6%, transparent 14%),
      linear-gradient(160deg, var(--road-mid) 0%, var(--road-dark) 55%, #3d3532 100%);
  }
  .ad__headline {
    position: absolute; left: 0; right: 0; top: 58px;
    text-align: center; color: var(--white);
    font-family: "Rubik Dirt", "Arial Black", sans-serif;
    text-transform: uppercase; line-height: 1;
  }
  .ad__headline-main { display: block; font-size: 94px; letter-spacing: 3px; }
  .ad__headline-sub { display: block; font-size: 60px; letter-spacing: 2px; margin-top: 8px; }
  .ad__divider {
    position: absolute; left: 733px; top: 522px; width: 273px; height: 12px;
    background: var(--white);
  }
  .ad__mission {
    position: absolute; left: 0; top: 505px; width: 733px; height: 150px;
    background: var(--ad-yellow);
    box-shadow: 10px 8px 0 var(--band-shadow);
    padding: 22px 40px 0 46px;
  }
  .ad__mission-text {
    font-family: "Arimo", Arial, sans-serif; font-weight: 700;
    font-size: 25px; line-height: 1.3; color: var(--ink);
  }
  .ad__mission-url {
    position: absolute; right: 48px; bottom: 14px;
    font-family: "Open Sans", Arial, sans-serif; font-size: 22px; color: var(--band-green);
  }
  .brand {
    display: flex; align-items: center; gap: 14px;
    font-family: "Arimo", Arial, sans-serif; font-weight: 700;
    color: var(--cream); line-height: 1.05; text-transform: uppercase;
  }
  .brand__dot { flex: none; border-radius: 50%; background: var(--logo-yellow); }
  .ad__brand { position: absolute; left: 755px; top: 565px; font-size: 26px; }
  .ad__brand .brand__dot { width: 34px; height: 34px; }
  .ad__footer {
    position: absolute; left: 46px; top: 668px;
    font-family: "Open Sans", Arial, sans-serif; font-size: 18px; line-height: 1.35;
    color: var(--white);
  }
  .ad__footer-url { color: var(--logo-yellow); }
  .ad__social {
    position: absolute; right: 24px; top: 672px;
    display: flex; align-items: center; gap: 14px;
  }
  .ad__social-label {
    font-family: "Arimo", Arial, sans-serif; font-weight: 700; font-size: 22px; color: var(--white);
    margin-right: 6px;
  }
  .ad__social-icon { width: 44px; height: 44px; display: block; }
  .signature-brand { position: absolute; left: 660px; top: 1025px; font-size: 46px; gap: 22px; }
  .signature-brand .brand__dot { width: 60px; height: 60px; }
</style>
</head>
<body>
  <section class="ad">
    <div class="ad__photo" role="img" aria-label="Photograph of a little girl in a red and white outfit lying on the curb of a grey city street"></div>
    <h1 class="ad__headline">
      <span class="ad__headline-main">Street Children</span>
      <span class="ad__headline-sub">Whose Responsibility?</span>
    </h1>
    <div class="ad__divider"></div>
    <div class="ad__mission">
      <p class="ad__mission-text">Give every child in the world the opportunity to live a happy and healthy life free of poverty exploitation and violence.</p>
      <span class="ad__mission-url">www.lenterabocah.org</span>
    </div>
    <div class="brand ad__brand">
      <span>Lentera Bocah<br>Foundation</span>
      <span class="brand__dot"></span>
    </div>
    <p class="ad__footer">Donate to GIRO 2749 t.a.v. Stichting Lentera Bocah<br>or financial adopt a child on <span class="ad__footer-url">www.lenterabocah.org</span></p>
    <div class="ad__social">
      <span class="ad__social-label">Follow us on</span>
      <svg class="ad__social-icon" viewBox="0 0 44 44" aria-label="Social network"><circle cx="22" cy="22" r="21" fill="var(--logo-yellow)"/></svg>
      <svg class="ad__social-icon" viewBox="0 0 44 44" aria-label="Social network"><circle cx="22" cy="22" r="21" fill="var(--logo-yellow)"/></svg>
    </div>
  </section>

  <div class="brand signature-brand">
    <span>Lentera Bocah<br>Foundation</span>
    <span class="brand__dot"></span>
  </div>
</body>
</html>
```